New young doctors office business card

Doctor's office
Hello:
My name is Dr. Eduardo Maximino Ortega Benavides. I need a business card for my new office located within a hospital. The name of the hospital is "Hospital Almendral". Although the hospital logo and name must be included in the business card, please make me a personal logo for myself. The logo might be maybe my name in a stylish font, or my initials (EMOB) or something like that. Im more inclined to a font logo, rather than a image logo, but a good one might change my mind. The info on my business card is going to be in spanish. The following info must be included please (the info within parenthesis is not to be included, it is provided for you to understand it since it's in spanish, so you can properly place it on the card):
-Dr. Eduardo Maximino Ortega Benavides (my name)
-Medicina general (My specialty)
-Hospital Almendral (The name of the hospital where my office is)
-Calle Tomás Ocampo #247 Col. Almendral (address)
-Tel 471-5836 (Office phone)
-Sábado y domingo 10:00 am a 10:00pm (Office hours)
-Emergencias: 555-917-4402 (Emergency phone)
-maximinoob@correoficticio.mx (email)
-English Spoken
So, that's all the info i need to be on the business card. Although it's a business card for a doctor's office, i dont want it to be a boring, plain business card. Make it eye-catchy and stylish please. As i said, the hospital logo must be included. You'll find it on the heading of the PDF file i attached, but dont make it the center of attention.
Physician
Hello:My name is Dr. Eduardo Maximino Ortega Benavides. I need a business card for my new office located within a hospital. The name of the hospital is "Hospital Almendral". Although the hospital logo and name must be included in the business card, please make me a personal logo for myself. The logo might be maybe my name in a stylish font, or my initials (EMOB) or something like that. Im more inclined to a font logo, rather than a image logo, but a good one might change my mind. The info on my business card is going to be in spanish. The following info must be included please (the info within parenthesis is not to be included, it is provided for you to understand it since it's in spanish, so you can properly place it on the card):-Dr. Eduardo Maximino Ortega Benavides (my name)-Medicina general (My specialty)-Hospital Almendral (The name of the hospital where my office is)-Calle Tomás Ocampo #247 Col. Almendral (address)-Tel 471-5836 (Office phone)-Sábado y domingo 10:00 am a 10:00pm (Office hours)-Emergencias: 555-917-4402 (Emergency phone)-maximinoob@correoficticio.mx (email)-English Spoken So, that's all the info i need to be on the business card. Although it's a business card for a doctor's office, i dont want it to be a boring, plain business card. Make it eye-catchy and stylish please. As i said, the hospital logo must be included. You'll find it on the heading of the PDF file i attached, but dont make it the center of attention.

```html
<!DOCTYPE html>
<html lang="es">
<head>
<meta charset="utf-8">
<title>Tarjeta de presentación – Dr. Eduardo Maximino Ortega Benavides</title>
<link rel="stylesheet" href="https://fonts.googleapis.com/css2?family=Lato:wght@400;700;900&display=swap">
<style>
  :root {
    --backdrop: #2a2b2d;
    --card: #1d1e20;
    --card-back: #1a1b1d;
    --ink: #ffffff;
    --rule: #cfcfcf;
    --hospital-blue: #1b3d9e;
  }
  * { box-sizing: border-box; margin: 0; padding: 0; }
  html, body {
    width: 1200px; height: 1108px; overflow: hidden;
    background: var(--backdrop);
    font-family: "Lato", sans-serif;
  }
  .stage {
    position: relative; width: 1200px; height: 1108px;
    display: flex; justify-content: center; align-items: center; gap: 60px;
  }
  .card {
    width: 420px; height: 680px; border-radius: 26px;
    box-shadow: 0 18px 40px rgba(0,0,0,.45);
    position: relative;
  }
  .card--front {
    background: var(--card); color: var(--ink);
    display: flex; flex-direction: column; align-items: center;
    padding-top: 78px; text-align: center;
  }
  .monogram {
    width: 290px; height: 240px; border: 9px solid var(--ink);
    display: flex; align-items: center; justify-content: center;
    font-weight: 900; font-size: 78px; letter-spacing: 2px;
  }
  .doctor-name { margin-top: 40px; font-weight: 700; font-size: 20px; }
  .specialty, .info { font-size: 18px; line-height: 1.3; }
  .rule { width: 300px; height: 1px; background: var(--rule); margin: 8px 0; }
  .hospital-upper { text-transform: uppercase; }
  .card--back {
    background: var(--card-back);
    display: flex; flex-direction: column; align-items: center; justify-content: center; gap: 22px;
  }
  .hospital-mark {
    width: 34px; height: 34px; background: var(--hospital-blue);
  }
  .hospital-name {
    color: var(--hospital-blue); font-weight: 700; font-size: 38px;
  }
</style>
</head>
<body>
<main class="stage">
  <section class="card card--front">
    <div class="monogram">EMOB</div>
    <p class="doctor-name">Dr. Eduardo Maximino Ortega Benavides</p>
    <p class="specialty">Medicina general</p>
    <div class="rule"></div>
    <p class="info hospital-upper">Hospital Almendral</p>
    <p class="info">Calle Tomás Ocampo #247 Col. Almendral</p>
    <div class="rule"></div>
    <p class="info">471-5836</p>
    <p class="info">maximinoob@correoficticio.mx</p>
    <div class="rule"></div>
    <p class="info">Sábado y domingo 10:00 am a 10:00pm</p>
    <p class="info">Emergencias: 555-917-4402</p>
  </section>
  <section class="card card--back">
    <div class="hospital-mark"></div>
    <p class="hospital-name">Hospital Almendral</p>
  </section>
</main>
</body>
</html>
```